Financial cloud based software needs a print design for a trade show booth

We have a cloud based system that captures, values and reports financial instruments. Our client base is medium sized corporates who use derivatives for hedging their financial exposures. We are showcasing our software at a conference and need a design that can be printed and used on our booth. The print size will be 2176mm(w) x 915mm (h). The conference is aimed at accountants. The design must incorporate the following bullet points:

• CVA/DVA (AASB 13 compliant)
• Independent valuations
• FX, interest rates and commodities
• Low monthly subscription

The design also needs to incorporate the attached Tilda's Gate and Varnlow logos. I have also attached a word doc that gives a basic layout. I'd also like to use the Varnlow "blue" as the background colour which goes from:
CMYK: 50, 0, 0, 0, RGB: 108, 206, 245 to
CMYK: 85, 50, 0, 0, RGB: 27,117,186
I have attached the brand guide fyi.
It would be good to incorporate the website address in the design somewhere too (www.varnlowpro-example.com).

Industry/Entity Type

Financial

```html
<!DOCTYPE html>
<html lang="en">
<head>
<meta charset="utf-8">
<title>Varnlow – Trade Show Booth Banner</title>
<link href="https://fonts.googleapis.com/css2?family=Arimo:wght@400;700&display=swap" rel="stylesheet">
<style>
  :root {
    --brand-blue-dark: #1b75ba;
    --brand-blue-light: #6ccef5;
    --navy: #262a68;
    --ink: #222222;
    --charcoal: #2b2b2b;
    --tick-grey: #7a7a7a;
    --white: #ffffff;
  }
  html, body {
    margin: 0;
    padding: 0;
    width: 1200px;
    height: 1000px;
    overflow: hidden;
    background: var(--white);
    font-family: "Arimo", Arial, sans-serif;
  }
  .canvas {
    position: relative;
    width: 1200px;
    height: 1000px;
  }
  .hero-band {
    position: absolute;
    left: 26px;
    top: 266px;
    width: 1145px;
    height: 347px;
    background: linear-gradient(90deg, var(--brand-blue-dark) 0%, #3d98d6 55%, var(--brand-blue-light) 100%);
  }
  .footer-band {
    position: absolute;
    left: 26px;
    top: 718px;
    width: 1145px;
    height: 28px;
    background: linear-gradient(90deg, var(--brand-blue-dark) 0%, #3d98d6 55%, var(--brand-blue-light) 100%);
  }
  .cloud {
    position: absolute;
    left: 290px;
    top: 285px;
    width: 545px;
    height: 292px;
  }
  .feature-list {
    position: absolute;
    left: 352px;
    top: 346px;
    margin: 0;
    padding: 0;
    list-style: none;
  }
  .feature-list li {
    display: flex;
    align-items: center;
    height: 39.2px;
    font-weight: 700;
    font-size: 23.5px;
    color: var(--ink);
    letter-spacing: 0.1px;
  }
  .tick {
    width: 26px;
    height: 30px;
    margin-right: 13px;
    flex: none;
  }
  .website {
    position: absolute;
    left: 46px;
    top: 672px;
    font-size: 23px;
    color: var(--ink);
  }
  .partner-name {
    position: absolute;
    left: 682px;
    top: 662px;
    display: flex;
    align-items: center;
    gap: 10px;
    font-size: 30px;
    font-weight: 700;
    color: var(--navy);
  }
  .partner-name .mark {
    width: 22px;
    height: 22px;
    background: var(--navy);
  }
  .brand-name {
    position: absolute;
    left: 893px;
    top: 628px;
    display: flex;
    align-items: flex-end;
    gap: 8px;
    font-size: 40px;
    font-weight: 700;
    color: var(--charcoal);
  }
  .brand-name .mark {
    width: 46px;
    height: 46px;
    border-radius: 50%;
    background: var(--brand-blue-dark);
    align-self: flex-start;
  }
  .brand-name span {
    line-height: 1;
    padding-top: 44px;
  }
</style>
</head>
<body>
<div class="canvas">
  <div class="hero-band"></div>

  <svg class="cloud" viewBox="0 0 545 292" aria-hidden="true">
    <g fill="#ffffff">
      <ellipse cx="272" cy="70" rx="92" ry="68"/>
      <ellipse cx="140" cy="128" rx="135" ry="108"/>
      <ellipse cx="405" cy="128" rx="135" ry="108"/>
      <ellipse cx="272" cy="150" rx="230" ry="105"/>
      <ellipse cx="285" cy="215" rx="150" ry="74"/>
      <ellipse cx="150" cy="185" rx="110" ry="60"/>
      <ellipse cx="405" cy="180" rx="125" ry="62"/>
    </g>
  </svg>

  <ul class="feature-list">
    <li><svg class="tick" viewBox="0 0 26 30"><path d="M2 17 L8 24 Q14 10 24 2" fill="none" stroke="var(--tick-grey)" stroke-width="3.5" stroke-linecap="round" stroke-linejoin="round"/></svg>CVA/DVA (AASB 13 compliant)</li>
    <li><svg class="tick" viewBox="0 0 26 30"><path d="M2 17 L8 24 Q14 10 24 2" fill="none" stroke="var(--tick-grey)" stroke-width="3.5" stroke-linecap="round" stroke-linejoin="round"/></svg>Independent valuations</li>
    <li><svg class="tick" viewBox="0 0 26 30"><path d="M2 17 L8 24 Q14 10 24 2" fill="none" stroke="var(--tick-grey)" stroke-width="3.5" stroke-linecap="round" stroke-linejoin="round"/></svg>FX, interest rates and commodities</li>
    <li><svg class="tick" viewBox="0 0 26 30"><path d="M2 17 L8 24 Q14 10 24 2" fill="none" stroke="var(--tick-grey)" stroke-width="3.5" stroke-linecap="round" stroke-linejoin="round"/></svg>Low monthly subscription</li>
  </ul>

  <div class="website">www.varnlowpro-example.com</div>

  <div class="partner-name"><div class="mark"></div>Tilda's Gate</div>

  <div class="brand-name"><div class="mark"></div><span>Varnlow</span></div>

  <div class="footer-band"></div>
</div>
</body>
</html>
```